Home page makeover

Take my existing home page, www.maplecrestharborline.com and redesign layout to look more current considering today's touch design prevalence.
Reuse existing elements or suggest improved ones if available.
I generally have average CSS and HTML skills using div containers, defining lists and using columns to create the code to support the layout.
Updates
Just wanted to send out a quick message to thank all of you for your submissions. Many of you offered nice designs, but unfortunately could only choose one.
Target Market(s)
Generally targeting individuals with some assets for retirement. Basically your average working professional or business owner.
Industry/Entity Type
It Support
Look and feel
Each slider illustrates characteristics of the customer's brand and the style your logo design should communicate.

```html
<!DOCTYPE html>
<html lang="en">
<head>
<meta charset="utf-8">
<title>Maplecrest Harborline – Home</title>
<link rel="stylesheet" href="https://fonts.googleapis.com/css2?family=Roboto:ital,wght@0,400;0,500;0,700;1,400&display=swap">
<style>
:root{
  --green-dark:#1c6412;
  --green-head:#1f5f17;
  --green-mid:#8cc63f;
  --green-band:#92d050;
  --red:#e3101b;
  --text:#555;
  --panel:#f7f7f7;
  --line:#dcdcdc;
  --footer:#3a3a3a;
  --footer-text:#e6e6e6;
  --white:#fff;
}
*{box-sizing:border-box;margin:0;padding:0}
html,body{width:946px;height:1200px;overflow:hidden}
body{font-family:"Roboto",Arial,sans-serif;color:var(--text);background:var(--white);position:relative}
.abs{position:absolute}
.site-header{position:absolute;left:0;top:0;width:946px;height:134px;background:linear-gradient(#fff,#efefef);border-bottom:1px solid #ddd}
.green-band{position:absolute;left:0;top:134px;width:946px;height:273px;background:var(--green-band)}
.brand{left:131px;top:18px;display:flex;align-items:center;gap:8px}
.brand-mark{width:40px;height:40px;background:var(--green-dark)}
.brand-name{font-size:24px;font-weight:700;color:var(--green-dark);line-height:1.05}
.account{left:614px;top:13px;width:109px;height:30px;background:var(--green-mid);color:var(--green-dark);font-size:10.5px;font-weight:500;display:flex;align-items:center;justify-content:center;letter-spacing:.3px}
.social{top:16px;width:22px;height:22px;border-radius:3px}
.main-nav{left:409px;top:74px;width:406px;display:flex;justify-content:space-between;font-size:10px;color:#222}
.main-nav a{color:inherit;text-decoration:none;height:25px;display:flex;align-items:center}
.main-nav a.active{background:var(--green-dark);color:#fff;padding:0 9px}
.slider-frame{left:131px;top:109px;width:685px;height:281px;background:#fff;border:1px solid #ccc;padding:4px}
.slider-photo{width:100%;height:100%;background:linear-gradient(180deg,#f4eb9e 0%,#e8cc72 45%,#caa24a 100%)}
.slide-card{left:148px;top:204px;width:300px;height:92px;background:rgba(255,250,232,.88);padding:6px 12px}
.slide-card h2{font-size:30px;font-weight:400;color:var(--green-head);line-height:1.05;margin-bottom:5px}
.slide-card p{font-size:14.5px;color:#333;line-height:22px;letter-spacing:.3px}
.slide-card b{color:var(--red);font-weight:500}
.dots{left:160px;top:361px;display:flex;gap:4px}
.dots i{width:12px;height:12px;border-radius:50%;background:#3d8a2c}
.dots i:first-child{background:#1d5a11}
.step{left:131px;width:393px;height:140px;background:var(--panel);border:1px solid var(--line)}
.step-photo{position:absolute;left:15px;top:15px;width:152px;height:107px}
.step-body{position:absolute;left:181px;top:14px;width:200px}
.step h3,.section-title{font-size:15.5px;font-weight:500;color:var(--green-head);letter-spacing:.4px}
.step p{font-size:10px;line-height:14.8px;margin-top:6px;color:var(--text)}
.more-link{display:block;margin-top:7px;font-size:10px;font-weight:500;color:var(--green-dark);letter-spacing:.3px}
.intro{left:538px;top:420px;width:278px}
.intro p{font-size:10px;line-height:16.7px;margin-top:8px}
.btn{display:inline-flex;align-items:center;justify-content:center;background:var(--green-mid);color:var(--green-dark);font-size:10px;font-weight:500;height:27px;padding:0 10px;letter-spacing:.3px}
.rule{height:1px;background:#c9c9c9}
.video{left:538px;top:679px;width:277px;height:191px;background:#000;border:1px solid #444}
.video-frame{position:absolute;left:34px;top:18px;width:206px;height:152px;background:linear-gradient(135deg,#d0d0d0,#777 60%,#eee)}
.video-bar{position:absolute;left:0;bottom:0;width:100%;height:18px;background:#1a1a1a;border-top:2px solid #555;color:#bbb;font-size:6px;display:flex;align-items:center;padding-left:40px}
.video-name{position:absolute;left:7px;top:5px;font-size:7px;color:#ddd}
.features{left:131px;top:890px;width:380px}
.features li{list-style:none;position:relative;padding-left:21px;font-size:10px;line-height:14.8px;margin-top:10px}
.features li svg{position:absolute;left:0;top:1px}
.col-divider{left:525px;top:893px;width:1px;height:200px;background:#ccc}
.testimonials{left:538px;top:890px;width:277px}
.quote{padding:16px 0 10px;font-size:9.8px;font-style:italic;line-height:15px;border-bottom:1px solid #ccc}
.quote:last-of-type{border-bottom:none}
.quote p{padding-left:10px}
.qmark{display:inline-block;font-size:34px;font-style:normal;font-weight:700;color:#b7dc8c;line-height:0;vertical-align:-12px}
.qmark.open{margin-left:-10px;margin-right:4px}
.qmark.close{margin-left:4px}
.quote cite{display:block;text-align:right;margin-top:2px;color:#444}
.quote cite b{color:var(--green-dark)}
.site-footer{position:absolute;left:0;top:1105px;width:946px;height:95px;background:var(--footer)}
.footer-brand{left:131px;top:1135px;font-size:20px;font-weight:700;color:#e8e8e8;display:flex;align-items:center;gap:8px}
.footer-brand span{width:30px;height:30px;background:#e8e8e8}
.footer-nav{left:444px;top:1136px;width:371px;display:flex;justify-content:space-between;font-size:9.5px;color:var(--footer-text)}
.copyright{left:503px;top:1166px;width:312px;text-align:right;font-size:8.8px;color:#d0d0d0;white-space:nowrap}
</style>
</head>
<body>
<header class="site-header"></header>
<div class="green-band"></div>

<div class="abs brand"><span class="brand-mark"></span><span class="brand-name">Maplecrest<br>Harborline</span></div>
<div class="abs account">SIGN UP &nbsp;|&nbsp; SIGN IN</div>
<span class="abs social" style="left:736px;background:#3b5b98"></span>
<span class="abs social" style="left:765px;background:#5fb9e6"></span>
<span class="abs social" style="left:793px;background:#c4281e"></span>

<nav class="abs main-nav">
  <a class="active">HOME</a><a>ABOUT US</a><a>SERVICES</a><a>FEATURES</a><a>TESTIMONIALS</a><a>CONTACT US</a>
</nav>

<section class="abs slider-frame">
  <div class="slider-photo" role="img" aria-label="Man with raised arms standing in a golden wheat field"></div>
</section>
<div class="abs slide-card">
  <h2>SIGN UP</h2>
  <p>Only <b>$19.99</b> For a One Year Membership</p>
  <p>Only <b>$9.99</b> Per Year After That</p>
</div>
<div class="abs dots"><i></i><i></i><i></i><i></i></div>

<article class="abs step" style="top:423px">
  <div class="step-photo" role="img" aria-label="Dollar bills, a pen and financial statements" style="background:linear-gradient(135deg,#c9cbb7,#8e927d 55%,#e4e6d8)"></div>
  <div class="step-body"><h3>IDENTIFY</h3><p>Aliquam molestie, mi et imperdiet euismod, dui purus auctor tellus, et interdum lacus lectus et ante. Sed ut perspiciatis unde omnis iste natus error sit voluptatem</p><a class="more-link">LEARN MORE</a></div>
</article>
<article class="abs step" style="top:577px">
  <div class="step-photo" role="img" aria-label="Laptop keyboard with reading glasses" style="background:linear-gradient(135deg,#3a3a3a,#9a9a9a 50%,#f2f2f2)"></div>
  <div class="step-body"><h3>PLAN</h3><p>Aliquam molestie, mi et imperdiet euismod, dui purus auctor tellus, et interdum lacus lectus et ante. Sed ut perspiciatis unde omnis iste natus error sit voluptatem</p><a class="more-link">LEARN MORE</a></div>
</article>
<article class="abs step" style="top:731px">
  <div class="step-photo" role="img" aria-label="Rope hammock on a porch by the sea" style="background:linear-gradient(180deg,#5d84bf,#b8c6d4 45%,#c9b79a 80%,#8b6f4c)"></div>
  <div class="step-body"><h3>RETIRE</h3><p>Aliquam molestie, mi et imperdiet euismod, dui purus auctor tellus, et interdum lacus lectus et ante. Sed ut perspiciatis unde omnis iste natus error sit voluptatem</p><a class="more-link">LEARN MORE</a></div>
</article>

<section class="abs intro">
  <h2 class="section-title">WELCOME TO OUR WEBSITE</h2>
  <p>Aliquam molestie, mi et imperdiet euismod, dui purus auctor tellus, et interdum lacus lectus et ante. Sed accumsan sollicitudin sapien, sit amet adipiscing turpis gravida ac. In congue, neque ac lobortis volutpat, libero mauris varius mi, vitae suscipit ipsum ligula vitae risus. Duis aliquam nibh a dui iaculis viverra id a velit. Vivamus egestas risus in magna varius commodo. Sed semper viverra egestas. Etiam pretium porttitor lectus, vel ornare neque porta volutpat.</p>
  <div style="margin-top:10px"><span class="btn">LEARN MORE</span></div>
  <div class="rule" style="margin-top:14px"></div>
  <h2 class="section-title" style="margin-top:12px">DEMO VIDEO</h2>
</section>
<div class="abs video">
  <span class="video-name">Demo.wmv</span>
  <div class="video-frame" role="img" aria-label="Video still of a laptop with glasses titled Plan"></div>
  <svg class="abs" style="left:116px;top:78px" width="44" height="30" viewBox="0 0 44 30"><rect width="44" height="30" rx="7" fill="#2a2a2a" opacity=".85"/><path d="M17 8 L29 15 L17 22Z" fill="#fff"/></svg>
  <div class="video-bar">0:00 / 0:26</div>
</div>

<section class="abs features">
  <h2 class="section-title">FEATURES</h2>
  <ul>
    <li><svg width="12" height="11" viewBox="0 0 12 11"><path d="M1 6 L4.5 9.5 L11 1" fill="none" stroke="#1c6412" stroke-width="2.4"/></svg>Identify and project your retirement needs and expectations including basic living expenses, housing costs, recreation, big ticket non-recurring items, medical and nursing home care.</li>
    <li><svg width="12" height="11" viewBox="0 0 12 11"><path d="M1 6 L4.5 9.5 L11 1" fill="none" stroke="#1c6412" stroke-width="2.4"/></svg>Identify and project all your sources of retirement income including retirement savings, other savings, pension plans, Social Security, life insurance and working part-time during retirement for a period of time.</li>
    <li><svg width="12" height="11" viewBox="0 0 12 11"><path d="M1 6 L4.5 9.5 L11 1" fill="none" stroke="#1c6412" stroke-width="2.4"/></svg>Strategize tapping into the equity of your real estate including swapping your primary residence for a different home or retirement area, or selling and renting.</li>
  </ul>
  <div style="margin-top:12px"><span class="btn">LEARN MORE</span></div>
</section>
<div class="abs col-divider"></div>

<section class="abs testimonials">
  <h2 class="section-title">TESTIMONIALS</h2>
  <div class="quote">
    <p><span class="qmark open">&ldquo;</span>This site is a great place to get a handle on your retirement strategy...<span class="qmark close">&rdquo;</span></p>
    <cite>- <b>Dana</b>, New Jersey</cite>
  </div>
  <div class="quote">
    <p><span class="qmark open">&ldquo;</span>I can see professionals using this site to validate their existing retirement plans...<span class="qmark close">&rdquo;</span></p>
    <cite>- <b>Owen</b>, New Jersey</cite>
  </div>
  <div style="text-align:right;margin-top:8px"><span class="btn" style="padding:0 18px">READ ALL</span></div>
</section>

<footer class="site-footer"></footer>
<div class="abs footer-brand"><span></span>Maplecrest Harborline</div>
<nav class="abs footer-nav"><a>HOME</a><a>ABOUT US</a><a>SERVICES</a><a>FEATURES</a><a>TESTIMONIALS</a><a>CONTACT US</a></nav>
<div class="abs copyright">Copyright © 2013. All Right Reserved &nbsp;|&nbsp; Privacy Policy &nbsp;|&nbsp; Terms &amp; Condition</div>
</body>
</html>
```